Online-Marketing Material für Schlüsseldienst
Zielgruppe
Wir bieten einen Schlüsseldienst mit Montagen im Bereich Sicherheitstechnik sowie Öffnungen jeder Art
Aufgabenstellung
Suche ein Stimmungsbild für den Kopfbereich unter der Navigation (730x160px). Design soll zur Seite passen, bitte vorhandene URL ansehen. Bild muss auch auf auf kleinem Viewport mobile funktionieren. Die Farben sollen entsprechend passen. Es könnte auch eine Collage sein, ähnlich wie aktuell von mir selbst gemacht(kesselwerk-tuerhilfe.example), natürlich nicht so stupide. Bitte Seite mit dem Browser verkleinern um das Bild auf seine Funktionalität zu überprüfen. Thema der Collage/des Stimmungsbildes im Kopfbereich könnten Montagen, Schlüssel, Schlüssel, Einbruchschutz, Autoschlüssel, Türöffnungen, Tresoröffnungen, Notdienst oder ähnliches sein.
Außerdem brauche ich entsprechend zu dem Stimmungsbild noch ein Nexora Local Profil Cover Photo in der Größe 1024 x 576 pixels (16:9 aspect ratio). Dies soll als Titelbild für mein Local Business dienen.

```html
<!DOCTYPE html>
<html lang="de">
<head>
<meta charset="utf-8">
<title>Ihre Sicherheit ist unser Geschäft</title>
<link href="https://fonts.googleapis.com/css2?family=Roboto+Condensed:wght@700;800&display=swap" rel="stylesheet">
<style>
  :root {
    --teal: #1b6a62;
    --teal-band: rgba(27, 106, 98, 0.88);
    --lime: #c9dd2c;
    --ink: #2b2b2b;
    --white: #ffffff;
  }
  * { box-sizing: border-box; margin: 0; padding: 0; }
  html, body { width: 1200px; height: 677px; overflow: hidden; background: var(--white); }
  .cover {
    position: relative;
    width: 1200px;
    height: 677px;
    overflow: hidden;
    background: var(--white);
    font-family: "Roboto Condensed", "Arial Narrow", sans-serif;
  }
  .tile { position: absolute; overflow: hidden; }
  .tile-door    { left: 404px; top: 0;     width: 411px; height: 340px; background: linear-gradient(120deg, #4d5f6d 0%, #8a9aa6 45%, #c9a48a 70%, #6f8fa3 100%); }
  .tile-cylinder{ left: 826px; top: 0;     width: 374px; height: 340px; background: linear-gradient(135deg, #e6e8ea 0%, #bfc4c8 50%, #d7b79f 80%, #eceeef 100%); }
  .tile-carkey  { left: 404px; top: 352px; width: 411px; height: 325px; background: linear-gradient(150deg, #7d8185 0%, #4a4d50 45%, #2a2b2d 75%, #6a6d70 100%); }
  .tile-worker  { left: 826px; top: 352px; width: 374px; height: 325px; background: radial-gradient(ellipse at 50% 70%, #5a7fb0 0%, #b49a85 35%, #e9e9e9 65%, #f2f2f2 100%); }
  .tile-label {
    position: absolute;
    left: 0;
    right: 0;
    height: 59px;
    background: var(--teal-band);
    color: var(--white);
    font-weight: 700;
    font-size: 44px;
    line-height: 59px;
    text-align: right;
    padding-right: 22px;
    letter-spacing: 0.2px;
  }
  .tile-top .tile-label { top: 248px; }
  .tile-bottom .tile-label { top: 232px; }
  .tile-worker .tile-label { text-align: center; padding-right: 0; }
  .arrow-panel { position: absolute; left: 0; top: 0; }
  .headline {
    position: absolute;
    left: 0;
    top: 0;
    width: 520px;
    height: 677px;
  }
  .headline span {
    position: absolute;
    font-weight: 800;
    font-size: 70px;
    line-height: 1;
    text-transform: uppercase;
    white-space: nowrap;
  }
  .line-plain { color: var(--white); }
  .line-accent { color: var(--ink); }
  .accent-bar { position: absolute; left: 0; background: var(--lime); }
  .bar-1 { top: 267px; width: 452px; height: 79px; }
  .bar-2 { top: 440px; width: 434px; height: 77px; }
  .l1 { left: 82px;  top: 198px; }
  .l2 { left: 40px;  top: 272px; }
  .l3 { left: 125px; top: 372px; }
  .l4 { left: 58px;  top: 444px; }
</style>
</head>
<body>
<div class="cover">
  <div class="tile tile-top tile-door" role="img" aria-label="Foto: Handwerker öffnet ein Türschloss">
    <div class="tile-label">Türöffnungen</div>
  </div>
  <div class="tile tile-top tile-cylinder" role="img" aria-label="Foto: Hand mit Schließzylinder und Schlüssel">
    <div class="tile-label">Schließanlagen</div>
  </div>
  <div class="tile tile-bottom tile-carkey" role="img" aria-label="Foto: Klappschlüssel eines Autos">
    <div class="tile-label">Autoschlüssel</div>
  </div>
  <div class="tile tile-bottom tile-worker" role="img" aria-label="Foto: lächelnder Handwerker mit Schraubenschlüssel">
    <div class="tile-label">u.v.m.</div>
  </div>

  <svg class="arrow-panel" width="530" height="677" viewBox="0 0 530 677" aria-hidden="true">
    <polygon points="0,0 393,0 516,338 393,677 0,677" fill="#1b6a62" stroke="#ffffff" stroke-width="6" stroke-linejoin="miter"/>
  </svg>

  <div class="headline">
    <div class="accent-bar bar-1"></div>
    <div class="accent-bar bar-2"></div>
    <span class="line-plain l1">Ihre</span>
    <span class="line-accent l2">Sicherheit</span>
    <span class="line-plain l3">Ist unser</span>
    <span class="line-accent l4">Geschäft</span>
  </div>
</div>
</body>
</html>
```